Business card for a new cabinet shop company named Torvane Cabinets for high end cabinets

Design a business card, thinking dark rich green with colours to speak of high end luxury ie; cream, gold, black possibly

Miles Harwick
Director Craftsman
Email: info@torvanecabinets.com.au
Instagram : @torvane.cabinets

```html
<!DOCTYPE html>
<html lang="en">
<head>
<meta charset="utf-8">
<title>Torvane Cabinets — Business Card</title>
<link rel="stylesheet" href="https://fonts.googleapis.com/css2?family=Poppins:wght@300;400;700&display=swap">
<style>
  :root {
    --page: #fefefe;
    --green-deep: #214c3e;
    --green-mid: #2a5a4b;
    --green-glow: #33695a;
    --gold: #c9ab65;
    --ink-green: #1f4a3b;
    --cream: #f4efe2;
    --white: #ffffff;
  }
  * { box-sizing: border-box; margin: 0; padding: 0; }
  html, body {
    width: 1200px; height: 1200px; overflow: hidden;
    background: var(--page);
    font-family: "Poppins", sans-serif;
  }
  .stage { position: relative; width: 1200px; height: 1200px; }

  .card {
    position: absolute;
    width: 348px; height: 199px;
    border-radius: 22px;
    overflow: hidden;
    background: var(--green-deep);
  }
  .card-texture {
    position: absolute; inset: 0;
  }
  .card--front { left: 243px; top: 504px; }
  .card--front .card-texture {
    background: radial-gradient(ellipse 62% 70% at 52% 42%, var(--green-glow) 0%, var(--green-mid) 45%, var(--green-deep) 100%);
  }
  .card--back { left: 617px; top: 505px; }
  .card--back .card-texture {
    background: radial-gradient(ellipse 70% 80% at 22% 32%, var(--green-glow) 0%, var(--green-mid) 48%, var(--green-deep) 100%);
  }

  /* Front */
  .front-brand {
    position: absolute; left: 0; right: 0; top: 58px;
    display: flex; align-items: center; justify-content: center; gap: 10px;
  }
  .brand-square {
    width: 18px; height: 18px;
    border: 1.5px solid var(--gold);
  }
  .brand-name {
    color: var(--gold);
    font-weight: 400;
    font-size: 24px;
    letter-spacing: 0.5px;
    line-height: 1;
  }
  .web-band {
    position: absolute; left: 0; right: 0; top: 148px; height: 20px;
    background: var(--gold);
    display: flex; align-items: center; justify-content: center;
    color: var(--ink-green);
    font-size: 9.5px; letter-spacing: 2.6px; font-weight: 400;
  }

  /* Back */
  .name-band {
    position: absolute; left: 0; top: 77px; width: 188px; height: 44px;
    background: var(--gold);
  }
  .person-name {
    position: absolute; left: 16px; top: 6px;
    color: var(--ink-green);
    font-weight: 700; font-size: 19px; line-height: 1.1;
  }
  .person-role {
    position: absolute; right: 30px; top: 27px;
    color: var(--cream);
    font-weight: 300; font-size: 10.5px; line-height: 1.1;
  }
  .contact-list {
    position: absolute; left: 16px; top: 130px;
    list-style: none;
  }
  .contact-item {
    display: flex; align-items: center; gap: 7px;
    height: 18px;
    color: var(--white);
    font-size: 10.6px; font-weight: 300;
  }
  .contact-icon { width: 11px; height: 11px; flex: none; }
  .back-brand {
    position: absolute; left: 232px; top: 84px; width: 100px;
    text-align: center;
    color: var(--gold);
    font-weight: 400; font-size: 17px; line-height: 1.15;
  }
</style>
</head>
<body>
<main class="stage">

  <section class="card card--front" aria-label="Business card front">
    <div class="card-texture" role="img" aria-label="Deep green background with a faint hexagon texture"></div>
    <div class="front-brand">
      <span class="brand-square" aria-hidden="true"></span>
      <span class="brand-name">Torvane Cabinets</span>
    </div>
    <div class="web-band">www.torvanecabinets.com.au</div>
  </section>

  <section class="card card--back" aria-label="Business card back">
    <div class="card-texture" role="img" aria-label="Deep green background with a faint hexagon texture"></div>
    <div class="name-band">
      <h1 class="person-name">Miles Harwick</h1>
      <p class="person-role">Director Craftsman</p>
    </div>
    <ul class="contact-list">
      <li class="contact-item">
        <svg class="contact-icon" viewBox="0 0 12 12" aria-hidden="true">
          <path d="M1 5 L6 1.5 L11 5 V11 H1 Z M1 5 L6 8.5 L11 5 M1 11 L5 7.5 M11 11 L7 7.5" fill="none" stroke="#c9ab65" stroke-width="0.8" stroke-linejoin="round"/>
        </svg>
        <span>info@torvanecabinets.com.au</span>
      </li>
      <li class="contact-item">
        <svg class="contact-icon" viewBox="0 0 12 12" aria-hidden="true">
          <circle cx="6" cy="6" r="4.8" fill="none" stroke="#c9ab65" stroke-width="0.8"/>
        </svg>
        <span>@torvane.cabinets</span>
      </li>
    </ul>
    <div class="back-brand">Torvane<br>Cabinets</div>
  </section>

</main>
</body>
</html>
```